Business card for law firm

Need business card for new law firm. Think confident, authoritative, conservative, but not stuffy or old-fashioned.

Contact Information for Business Card

Content for card - logo (uploaded), plus the following:

Paul Wexbury (larger font)
Managing Partner (larger font, but not as large as name)
Level 9, 41 Tansy Lane
Sydney NSW 2000
Main Tel 02 7346 2190
Direct Tel 02 6273 4415
Email paul@qvlegal.com.au
www.qvlegal.com.au

Letterhead design should include logo plus:
Level 9, 41 Tansy Lane
Sydney NSW 2000
Tel 02 6273 4415
www.qvlegal.com.au

```html
<!DOCTYPE html>
<html lang="en">
<head>
<meta charset="utf-8">
<title>Quayvale Lawyers — Business Card</title>
<link rel="stylesheet" href="https://fonts.googleapis.com/css2?family=Open+Sans:wght@400;700&display=swap">
<style>
  :root {
    --navy: #0d1f5c;
    --ink: #111111;
    --text: #2a2a2a;
    --rule: #b9b9b9;
    --card: #ffffff;
    --card-edge: #a9aaac;
    --bg-light: #eaebec;
    --bg-dark: #c4c5c8;
  }
  * { margin: 0; padding: 0; box-sizing: border-box; }
  html, body { width: 1200px; height: 1112px; overflow: hidden; }
  body {
    position: relative;
    background: linear-gradient(160deg, var(--bg-light) 0%, var(--bg-dark) 100%);
    font-family: "Open Sans", sans-serif;
    color: var(--text);
  }
  .card {
    position: absolute;
    width: 767px; height: 438px;
    background: var(--card);
    border: 1px solid var(--card-edge);
    border-radius: 30px;
    overflow: hidden;
  }
  .card--front { left: 77px; top: 80px; }
  .card--back { left: 356px; top: 580px; }

  .brand { position: absolute; text-align: center; color: var(--ink); font-weight: 400; }
  .brand__mark { display: block; margin: 0 auto; background: var(--navy); }
  .brand__name { display: block; line-height: 1; }
  .brand__name-main { display: block; letter-spacing: 0.06em; }
  .brand__name-sub { display: block; letter-spacing: 0.9em; margin-right: -0.9em; }

  .card--front .brand { left: 68px; top: 86px; width: 340px; }
  .card--front .brand__mark { width: 78px; height: 78px; margin-bottom: 30px; }
  .card--front .brand__name-main { font-size: 46px; }
  .card--front .brand__name-sub { font-size: 17px; margin-top: 12px; }

  .divider {
    position: absolute; left: 433px; top: 73px;
    width: 2px; height: 221px; background: var(--rule);
  }
  .contact { position: absolute; left: 461px; top: 74px; }
  .contact__name { color: var(--navy); font-weight: 700; font-size: 28px; line-height: 1.2; }
  .contact__title { font-size: 20px; margin-top: 6px; text-transform: uppercase; letter-spacing: 0.01em; }
  .contact__list { list-style: none; margin-top: 22px; }
  .contact__item { display: flex; align-items: center; font-size: 21px; line-height: 34px; }
  .contact__icon { width: 19px; height: 19px; margin-right: 7px; flex: none; }

  .band { position: absolute; left: 0; top: 0; width: 767px; height: 438px; }
  .address {
    position: absolute; left: 0; right: 0; top: 398px;
    text-align: center; color: #ffffff; font-size: 21px;
  }

  .card--back .brand { left: 0; right: 0; top: 56px; }
  .card--back .brand__mark { width: 96px; height: 96px; margin-bottom: 44px; }
  .card--back .brand__name-main { font-size: 54px; }
  .card--back .brand__name-sub { font-size: 20px; margin-top: 14px; }
  .web {
    position: absolute; left: 0; right: 0; top: 360px;
    text-align: center; font-size: 25px; letter-spacing: 0.18em; color: var(--text);
  }
  .web strong { color: var(--navy); font-weight: 700; }
</style>
</head>
<body>

<section class="card card--front">
  <svg class="band" viewBox="0 0 767 438" aria-hidden="true">
    <path d="M0 284 Q 360 420 640 377 Q 360 410 0 306 Z" fill="#0a0a0a"/>
    <path d="M0 318 Q 400 440 767 362 L767 438 L0 438 Z" fill="var(--navy)"/>
  </svg>

  <div class="brand">
    <span class="brand__mark"></span>
    <span class="brand__name">
      <span class="brand__name-main">QUAYVALE</span>
      <span class="brand__name-sub">LAWYERS</span>
    </span>
  </div>

  <div class="divider"></div>

  <div class="contact">
    <h1 class="contact__name">PAUL WEXBURY</h1>
    <p class="contact__title">Managing Partner</p>
    <ul class="contact__list">
      <li class="contact__item">
        <svg class="contact__icon" viewBox="0 0 20 20" aria-hidden="true"><circle cx="10" cy="10" r="8.5" fill="none" stroke="var(--navy)" stroke-width="1.6"/><path d="M7 5.5c-1.5 2.5-.5 6.5 3 9l1.8-1.6-1.8-1.8-1 .6c-1-1-1.4-2.4-1.2-3.6l1.2-.2-.4-2.4z" fill="var(--navy)"/></svg>
        02 7346 2190(Main)
      </li>
      <li class="contact__item">
        <svg class="contact__icon" viewBox="0 0 20 20" aria-hidden="true"><circle cx="10" cy="10" r="8.5" fill="none" stroke="var(--navy)" stroke-width="1.6"/><path d="M7 5.5c-1.5 2.5-.5 6.5 3 9l1.8-1.6-1.8-1.8-1 .6c-1-1-1.4-2.4-1.2-3.6l1.2-.2-.4-2.4z" fill="var(--navy)"/></svg>
        02 6273 4415(Direct)
      </li>
      <li class="contact__item">
        <svg class="contact__icon" viewBox="0 0 20 20" aria-hidden="true"><path d="M1 8l9-6 9 6v10H1z" fill="var(--navy)"/><path d="M2 8.5l8 5 8-5" fill="none" stroke="#fff" stroke-width="1.4"/></svg>
        paul@qvlegal.com.au
      </li>
      <li class="contact__item">
        <svg class="contact__icon" viewBox="0 0 20 20" aria-hidden="true"><g fill="none" stroke="var(--navy)" stroke-width="1.4"><circle cx="10" cy="10" r="8.3"/><ellipse cx="10" cy="10" rx="3.8" ry="8.3"/><path d="M1.7 10h16.6M3 5.5h14M3 14.5h14"/></g></svg>
        www.qvlegal.com.au
      </li>
    </ul>
  </div>

  <p class="address">Level 9, 41 Tansy Lane, Sydney NSW 2000</p>
</section>

<section class="card card--back">
  <div class="brand">
    <span class="brand__mark"></span>
    <span class="brand__name">
      <span class="brand__name-main">QUAYVALE</span>
      <span class="brand__name-sub">LAWYERS</span>
    </span>
  </div>
  <p class="web">www.<strong>qvlegal</strong>.com.au</p>
</section>

</body>
</html>
```